Property letting UK website

I need a web design for a new Property letting company in the UK. I already have a logo that was produced and won by a pixel harbor logo designer last week.

I like modern designs and require ease of functionality and usage. I already have a domain name registered so need to be able to link to that domain.

Regards,

Miles.

Target Market(s)

UK property

Industry/Entity Type

It Company

Number of Pages Required

5+ page

Requirements
Must have
• Home page, Current properties to let page, About us page, Contact us page, Testimonials page and ability to link to chirpnet and Friendlane account.

```html
<!DOCTYPE html>
<html lang="en">
<head>
<meta charset="utf-8">
<title>Hearthway Lettings</title>
<link href="https://fonts.googleapis.com/css2?family=Montserrat:wght@400;500;600;700&family=Open+Sans:ital,wght@0,400;0,600;0,700;1,400&display=swap" rel="stylesheet">
<style>
:root{
  --blue:#0aa3e6;
  --blue-dark:#078ccb;
  --black:#050505;
  --ink:#1a1a1a;
  --grey-bg:#ececec;
  --text:#333;
  --muted:#777;
  --white:#fff;
  --field:#ececec;
}
*{box-sizing:border-box;margin:0;padding:0}
html,body{width:1200px;height:3475px;overflow:hidden}
body{position:relative;background:var(--white);font-family:"Open Sans",Arial,sans-serif;color:var(--text)}
.abs{position:absolute}
h2,h3,h4,.nav a,.btn{font-family:"Montserrat",Arial,sans-serif}

/* header */
.site-header{left:0;top:0;width:1200px;height:115px;background:var(--black)}
.brand{left:109px;top:26px;display:flex;align-items:center;gap:12px}
.brand-mark{width:26px;height:26px;border-radius:50%;background:var(--blue)}
.brand-name{font-family:"Montserrat",sans-serif;font-weight:500;font-size:30px;color:var(--white);letter-spacing:1px}
.nav{right:118px;top:68px;display:flex;gap:40px}
.nav a{color:var(--white);text-decoration:none;font-size:17px;font-weight:600}
.nav a.active{color:var(--blue)}

/* hero */
.hero{left:0;top:115px;width:1200px;height:529px;background:linear-gradient(180deg,#2b3a52 0%,#5a5550 45%,#2a2a2e 100%)}
.dots{display:flex;gap:8px}
.dots span{width:14px;height:14px;border-radius:50%;background:var(--white)}
.dots span.on{background:var(--blue)}
.hero .dots{position:absolute;left:563px;top:483px}

/* properties */
.band{left:0;top:644px;width:1200px;height:84px;background:var(--blue)}
.band h2{position:absolute;left:109px;top:26px;color:var(--white);font-size:23px;font-weight:600}
.band-pointer{left:209px;top:726px}
.properties{left:0;top:728px;width:1200px;height:829px;background:var(--grey-bg)}
.card{position:absolute;width:317px}
.card-photo{width:317px;height:197px;position:relative;overflow:hidden}
.tag{position:absolute;left:-28px;top:18px;width:120px;height:26px;transform:rotate(-45deg);color:var(--white);font-size:11px;font-weight:600;text-align:center;line-height:26px}
.tag.rental{background:#7cc520}
.tag.leased{background:#c99a18}
.card h3{font-size:14px;font-weight:700;color:var(--ink);margin-top:24px}
.card p{font-size:12.5px;line-height:19px;color:#444;margin-top:8px}
.btn-dark{display:inline-block;background:var(--black);color:var(--white);font-size:13px;padding:0 10px;height:28px;line-height:28px;margin-top:12px;font-family:"Open Sans",sans-serif}
.btn-blue{background:var(--blue);color:var(--white);text-align:center;font-weight:600}
.view-all{left:470px;top:1478px;width:260px;height:47px;line-height:47px;font-size:18px}

/* about */
.about-photo{left:0;top:1557px;width:1200px;height:575px;background:linear-gradient(90deg,#c9ccd3 0%,#8e8a86 35%,#c4c7cc 60%,#9b9894 100%)}
.about-box{left:695px;top:1615px;width:394px;height:486px;background:rgba(10,10,10,.9);padding:32px 32px}
.about-box h2{color:var(--blue);font-size:24px;font-weight:500}
.about-box p{color:#eee;font-size:13.5px;line-height:25px;margin-top:20px}
.about-box .btn-blue{display:inline-block;width:121px;height:35px;line-height:35px;font-size:14px;margin-top:26px}

/* testimonials */
.testimonials{left:0;top:2132px;width:1200px;height:315px;background:var(--blue)}
.testimonials h2{position:absolute;width:1200px;top:28px;text-align:center;color:var(--white);font-size:23px;font-weight:600}
.avatar{position:absolute;left:162px;top:99px;width:162px;height:149px;border-radius:12px;border:4px solid var(--white);background:linear-gradient(160deg,#c9d2d8,#8a7460)}
.quote-mark{position:absolute;left:338px;top:62px}
.testimonials blockquote{position:absolute;left:352px;top:128px;width:700px;color:var(--white);font-style:italic;font-size:14.5px;line-height:25px}
.author{position:absolute;right:111px;top:240px;text-align:right;color:var(--white)}
.author strong{display:block;font-style:italic;font-size:17px;font-family:"Montserrat",sans-serif}
.author span{font-size:14px}
.testimonials .dots{position:absolute;left:558px;top:287px}

/* contact */
.contact-title{left:0;top:2484px;width:1200px;text-align:center;color:var(--blue);font-size:25px;font-weight:500}
.col-title{font-size:17px;font-weight:600;color:var(--ink)}
.form-box{left:113px;top:2641px;width:471px;height:482px;background:#f6f6f6;border-radius:10px}
.form-notch{left:160px;top:2620px}
.label{font-size:12.5px;color:#333}
.field{background:var(--field);border-radius:10px;border:1px solid #e2e2e2}
.submit{left:153px;top:3070px;width:90px;height:34px;border-radius:8px;line-height:34px;font-size:14px}
.map{left:630px;top:2648px;width:459px;height:218px;background:linear-gradient(135deg,#e8e3d3,#f2efe3 50%,#dfe5cf)}
.address{left:630px;top:2950px;font-size:14.5px;line-height:22px;color:#222}

/* footer */
.site-footer{left:0;top:3174px;width:1200px;height:301px;background:var(--black)}
.foot-col h4{color:var(--blue);font-size:14.5px;font-weight:500}
.foot-col ul{list-style:none;margin-top:20px}
.foot-col li{color:var(--white);font-size:12.5px;line-height:24px}
.foot-col p{color:var(--white);font-size:12.5px;line-height:20px;margin-top:18px;width:230px}
.foot-input{position:absolute;width:222px;height:27px;background:var(--white);font-size:11px;color:#999;padding:6px 8px}
.subscribe{position:absolute;width:99px;height:23px;border-radius:12px;line-height:23px;font-size:12.5px}
.social{display:flex;align-items:center;gap:58px;color:var(--white);font-size:12.5px;height:28px}
.social i{width:28px;height:28px;border-radius:50%;background:var(--white)}
.copyright{left:0;top:3434px;width:1200px;text-align:center;color:var(--white);font-size:11.5px}
</style>
</head>
<body>

<header class="abs site-header">
  <div class="abs brand"><span class="brand-mark"></span><span class="brand-name">Hearthway</span></div>
  <nav class="abs nav">
    <a class="active" href="#">Home</a>
    <a href="#">Current Properties</a>
    <a href="#">About Us</a>
    <a href="#">Testimonials</a>
    <a href="#">Contact Us</a>
  </nav>
</header>

<section class="abs hero" role="img" aria-label="Night-time aerial view of a city skyline with lit office towers">
  <div class="dots"><span class="on"></span><span></span><span></span><span></span></div>
</section>

<div class="abs band"><h2>Current Properties</h2></div>
<svg class="abs band-pointer" width="32" height="18" viewBox="0 0 32 18"><polygon points="0,0 32,0 16,18" fill="#0aa3e6"/></svg>

<section class="abs properties">
  <article class="card" style="left:109px;top:32px">
    <div class="card-photo" role="img" aria-label="Villa with a lit swimming pool at dusk" style="background:linear-gradient(160deg,#6f8fb3,#b0704a 55%,#2f8fb0)"><span class="tag rental">Rental</span></div>
    <h3>Neque porro quisquam est</h3>
    <p>There is no one who loves pain itself, who seeks after it and wants to have it, simply because it is pain</p>
    <span class="btn-dark">View Details</span>
  </article>
  <article class="card" style="left:442px;top:32px">
    <div class="card-photo" role="img" aria-label="White two-storey family house with a lawn" style="background:linear-gradient(180deg,#7aa6d6,#e8e8e4 55%,#5c8a3c)"><span class="tag leased">Leased</span></div>
    <h3>Neque porro quisquam est</h3>
    <p>There is no one who loves pain itself, who seeks after it and wants to have it, simply because it is pain</p>
    <span class="btn-dark">View Details</span>
  </article>
  <article class="card" style="left:774px;top:32px">
    <div class="card-photo" role="img" aria-label="Modern home with palm trees and an infinity pool at sunset" style="background:linear-gradient(180deg,#8a7fa8,#d9a98a 50%,#3a4e7a)"><span class="tag rental">Rental</span></div>
    <h3>Neque porro quisquam est</h3>
    <p>There is no one who loves pain itself, who seeks after it and wants to have it, simply because it is pain</p>
    <span class="btn-dark">View Details</span>
  </article>
  <article class="card" style="left:109px;top:384px">
    <div class="card-photo" role="img" aria-label="Brick suburban house with a green front lawn" style="background:linear-gradient(180deg,#6f9fd8,#a6704e 55%,#5e9a3a)"><span class="tag leased">Leased</span></div>
    <h3>Neque porro quisquam est</h3>
    <p>There is no one who loves pain itself, who seeks after it and wants to have it, simply because it is pain</p>
    <span class="btn-dark">View Details</span>
  </article>
  <article class="card" style="left:442px;top:384px">
    <div class="card-photo" role="img" aria-label="Mediterranean style house with palm trees" style="background:linear-gradient(180deg,#8fb8e0,#d8c6a6 55%,#5f7f3c)"><span class="tag leased">Leased</span></div>
    <h3>Neque porro quisquam est</h3>
    <p>There is no one who loves pain itself, who seeks after it and wants to have it, simply because it is pain</p>
    <span class="btn-dark">View Details</span>
  </article>
  <article class="card" style="left:774px;top:384px">
    <div class="card-photo" role="img" aria-label="Modern apartment block with balconies" style="background:linear-gradient(180deg,#9cc0e6,#b8b4ac 55%,#6a8a4a)"><span class="tag rental">Rental</span></div>
    <h3>Neque porro quisquam est</h3>
    <p>There is no one who loves pain itself, who seeks after it and wants to have it, simply because it is pain</p>
    <span class="btn-dark">View Details</span>
  </article>
</section>
<a class="abs btn btn-blue view-all">VIEW ALL PROPERTIES</a>

<section class="abs about-photo" role="img" aria-label="Group of smiling business people in an office"></section>
<div class="abs about-box">
  <h2>About Us</h2>
  <p>Lorem Ipsum is simply dummy text of the printing and typesetting industry. Lorem Ipsum has been the industry's standard dummy text ever since the 1500s, when an unknown printer took a galley of type and scrambled it to make a type specimen book. It has survived not only five centuries, but also the leap into electronic typesetting, remaining essentially unchanged. It was popularised in the 1960s with the release of Typeline sheets containing Lorem Ipsum passages, and more recently with desktop publishing software including versions of Lorem Ipsum.</p>
  <span class="btn btn-blue">Read More</span>
</div>

<section class="abs testimonials">
  <h2>Customer's Testimonials</h2>
  <div class="avatar" role="img" aria-label="Portrait of a client working on a laptop"></div>
  <svg class="quote-mark" width="56" height="48" viewBox="0 0 56 48"><g fill="#000"><path d="M4 44 V26 C4 12 10 4 22 2 L24 8 C16 10 13 15 13 22 H22 V44Z"/><path d="M32 44 V26 C32 12 38 4 50 2 L52 8 C44 10 41 15 41 22 H50 V44Z"/></g></svg>
  <blockquote>Lorem Ipsum is simply dummy text of the printing and typesetting industry. Lorem Ipsum has been the industry's standard dummy text ever since the 1500s, when an unknown printer took a galley of type and scrambled it to make a type specimen book. It has survived not only five centuries, but also the leap into electronic typesetting, remaining essentially unchanged.</blockquote>
  <div class="author"><strong>Daniel Brooks</strong><span>Owner ,London</span></div>
  <div class="dots"><span></span><span></span><span></span><span></span><span></span></div>
</section>

<h2 class="abs contact-title">Contact Us</h2>
<h3 class="abs col-title" style="left:109px;top:2574px">Contact Us</h3>
<h3 class="abs col-title" style="left:630px;top:2574px">Location</h3>

<svg class="abs form-notch" width="60" height="22" viewBox="0 0 60 22"><polygon points="0,22 30,0 60,22" fill="#f6f6f6"/></svg>
<div class="abs form-box"></div>
<span class="abs label" style="left:155px;top:2672px">Your Name *</span>
<div class="abs field" style="left:153px;top:2695px;width:389px;height:40px"></div>
<svg class="abs" style="left:508px;top:2706px" width="16" height="18" viewBox="0 0 16 18"><circle cx="8" cy="5" r="4" fill="#888"/><path d="M1 18c0-5 3-7 7-7s7 2 7 7z" fill="#888"/></svg>
<span class="abs label" style="left:155px;top:2752px">Your email address *</span>
<div class="abs field" style="left:153px;top:2776px;width:389px;height:40px"></div>
<span class="abs" style="left:508px;top:2784px;font-size:18px;color:#666">@</span>
<span class="abs label" style="left:155px;top:2833px">Your message</span>
<div class="abs field" style="left:153px;top:2857px;width:389px;height:190px"></div>
<svg class="abs" style="left:509px;top:2868px" width="16" height="12" viewBox="0 0 16 12"><rect width="16" height="12" rx="1" fill="#888"/><path d="M1 1l7 6 7-6" stroke="#eee" stroke-width="1.5" fill="none"/></svg>
<span class="abs btn btn-blue submit">› SUBMIT</span>

<div class="abs map" role="img" aria-label="Street map showing the office location"></div>
<h3 class="abs col-title" style="left:630px;top:2910px">Address</h3>
<address class="abs address" style="font-style:normal;top:2953px">Hearthway Lettings Ltd<br>42 Marlow Crescent<br>Bristol BS1 4QT<br>United Kingdom<br>Telephone: +44 117 496 0321<br>E-mail: hello@hearthwaylettings.example</address>

<footer class="abs site-footer">
  <div class="abs foot-col" style="left:109px;top:40px">
    <h4>Quick Links</h4>
    <ul><li>Home</li><li>About Us</li><li>Services</li><li>Service Plans</li><li>News</li><li>FAQ &amp; Wiki</li><li>Contact Us</li></ul>
  </div>
  <div class="abs foot-col" style="left:350px;top:40px">
    <h4>Support Links</h4>
    <ul><li>Legal Notice</li><li>Privacy Policy</li><li>Terms &amp; Conditions</li><li>Help</li></ul>
  </div>
  <div class="abs foot-col" style="left:593px;top:40px">
    <h4>Newsletter SignUp</h4>
    <p>Sign-up for our daily emails by entering your information below:</p>
  </div>
  <div class="foot-input" style="left:593px;top:130px">Name</div>
  <div class="foot-input" style="left:593px;top:172px">Enter Your E-Mail ID</div>
  <span class="btn btn-blue subscribe" style="left:716px;top:211px">Subscribe</span>
  <div class="abs foot-col" style="left:911px;top:40px">
    <h4>Connect With Us</h4>
  </div>
  <div class="abs social" style="left:912px;top:80px"><i></i>chirpnet</div>
  <div class="abs social" style="left:912px;top:118px"><i></i>Friendlane</div>
</footer>
<p class="abs copyright">Copyright ©2013 Hearthway Lettings&nbsp;&nbsp;- All rights reserved</p>

</body>
</html>
```